Halvorsen Construction Needs a Business Card

Our current business card is very bland, and since we have a new logo, we would like a new business card design to reflect our company. It can be a single-sided or two-sided card, but it is important that our contact information appears on the same side. I am attaching a copy of our old card and our new logo. If you need the logo in another format than the one I'm sending, please let me know. This is the information that we must have on our card, but not necessarily in any specific order:
1) Our logo
2) General Contractor
3) Dale Halvorsen, Owner
4) 482 Commerce Ridge Road, Centre, Alabama 35871
5) Office: 256-555-0147
7) Fax: 256-555-0148
8) Cell: 256-555-0193
9) halvorsenconstruction@qvl-mail.net
10) halvorsenconstruction-example.com (can be omitted if necessary)
Also, I will need files in a format that I can alter if any of the above information changes in the near future. Thank you in advance for your submissions!
Target Market(s)
Commercial and residential clients, architects, and subcontractors.
Industry/Entity Type
Business
Look and feel

```html
<!DOCTYPE html>
<html lang="en">
<head>
<meta charset="utf-8">
<title>Halvorsen Construction – Business Card</title>
<link rel="stylesheet" href="https://fonts.googleapis.com/css2?family=Exo+2:wght@400;500;600;800&display=swap">
<style>
  :root {
    --backdrop: #e7e5e1;
    --card-white: #ffffff;
    --charcoal: #323234;
    --amber: #fbb829;
    --text-light: #f2f2f2;
    --shadow: rgba(0, 0, 0, 0.18);
  }
  * { margin: 0; padding: 0; box-sizing: border-box; }
  html, body {
    width: 1200px;
    height: 901px;
    overflow: hidden;
    background: var(--backdrop);
    font-family: "Exo 2", sans-serif;
  }
  .canvas {
    position: relative;
    width: 1200px;
    height: 901px;
    display: flex;
    align-items: center;
    justify-content: center;
    gap: 40px;
  }
  .card {
    position: relative;
    width: 540px;
    height: 309px;
    border-radius: 22px;
    overflow: hidden;
    background: var(--card-white);
    box-shadow: 0 10px 28px var(--shadow);
  }
  .card-shapes {
    position: absolute;
    inset: 0;
    width: 100%;
    height: 100%;
  }
  .brand {
    position: absolute;
    display: flex;
    align-items: center;
    color: var(--charcoal);
    font-weight: 800;
    text-transform: uppercase;
    line-height: 1;
  }
  .brand-square {
    background: var(--charcoal);
    flex: none;
  }
  .brand-name span { display: block; }

  .card-contact .brand { left: 40px; top: 28px; gap: 10px; }
  .card-contact .brand-square { width: 30px; height: 30px; }
  .card-contact .brand-name { font-size: 21px; letter-spacing: 0.5px; }
  .card-contact .brand-name .brand-sub { font-size: 11px; letter-spacing: 6.4px; margin-top: 3px; }

  .card-logo .brand { left: 50%; top: 50%; transform: translate(-50%, -50%); gap: 16px; }
  .card-logo .brand-square { width: 52px; height: 52px; }
  .card-logo .brand-name { font-size: 40px; letter-spacing: 1px; }
  .card-logo .brand-name .brand-sub { font-size: 19px; letter-spacing: 13px; margin-top: 5px; }

  .contact-block {
    position: absolute;
    right: 28px;
    top: 126px;
    text-align: right;
    color: var(--text-light);
  }
  .person-name {
    font-size: 16px;
    font-weight: 600;
    letter-spacing: 1.5px;
    text-transform: uppercase;
    line-height: 1.2;
  }
  .person-title {
    font-size: 11px;
    font-weight: 400;
    margin-top: 2px;
  }
  .address {
    font-size: 11px;
    line-height: 1.3;
    margin-top: 8px;
    margin-right: 20px;
  }
  .contact-list {
    list-style: none;
    margin-top: 6px;
    font-size: 11px;
    line-height: 1;
  }
  .contact-list li {
    display: flex;
    justify-content: flex-end;
    align-items: center;
    gap: 8px;
    margin-top: 5px;
  }
  .contact-icon {
    width: 12px;
    height: 12px;
    flex: none;
    fill: var(--text-light);
  }
</style>
</head>
<body>
<main class="canvas">

  <section class="card card-contact" aria-label="Business card, contact side">
    <svg class="card-shapes" viewBox="0 0 540 309" preserveAspectRatio="none" aria-hidden="true">
      <path d="M0,88 Q200,218 540,-12 L540,309 L0,309 Z" fill="var(--amber)"/>
      <path d="M0,120 Q200,250 540,20 L540,309 L0,309 Z" fill="var(--charcoal)"/>
    </svg>

    <div class="brand">
      <div class="brand-square"></div>
      <div class="brand-name">
        <span>Halvorsen</span>
        <span class="brand-sub">Construction</span>
      </div>
    </div>

    <div class="contact-block">
      <p class="person-name">Dale Halvorsen</p>
      <p class="person-title">Owner · General Contractor</p>
      <p class="address">482 Commerce Ridge Road<br>Centre, Alabama 35871</p>
      <ul class="contact-list">
        <li>Office: 256-555-0147
          <svg class="contact-icon" viewBox="0 0 12 12"><path d="M2.5 1l2 2.2-1 1.3c.7 1.5 1.9 2.7 3.4 3.4l1.3-1 2.2 2-1.2 1.6C5 10.2 1.8 7 .9 2.3z"/></svg>
        </li>
        <li>Fax: 256-555-0148
          <svg class="contact-icon" viewBox="0 0 12 12"><path d="M1 3h10v8H1zM3 0h6v3H3zM2.5 5v1h2V5zm3 0v1h2V5zm-3 2v1h2V7zm3 0v1h2V7z"/></svg>
        </li>
        <li>Cell: 256-555-0193
          <svg class="contact-icon" viewBox="0 0 12 12"><path d="M3 1h6v10H3zM4 2v7h4V2z"/></svg>
        </li>
        <li>halvorsenconstruction@qvl-mail.net
          <svg class="contact-icon" viewBox="0 0 12 12"><path d="M0 2h12v8H0zm1 1v.4L6 7l5-3.6V3z"/></svg>
        </li>
        <li>halvorsenconstruction-example.com
          <svg class="contact-icon" viewBox="0 0 12 12"><path d="M6 0a6 6 0 110 12A6 6 0 016 0zm0 1.2a4.8 4.8 0 100 9.6 4.8 4.8 0 000-9.6zM1.5 5.5h9v1h-9zM5.5 1.5h1v9h-1z"/></svg>
        </li>
      </ul>
    </div>
  </section>

  <section class="card card-logo" aria-label="Business card, logo side">
    <div class="brand">
      <div class="brand-square"></div>
      <div class="brand-name">
        <span>Halvorsen</span>
        <span class="brand-sub">Construction</span>
      </div>
    </div>
  </section>

</main>
</body>
</html>
```